New Innovative Product needs a new business card design

We need a business card design for a new product line based in Michigan called "Lendwise Tailwind." We are a credit company by nature however this product should have a clean, simple, "zorvik-esque" feel. We have a few tag lines we use that could or could not be used...."All Referral Roads Lead to You" we use the attached pic in much or our marketing and also use both a white and/or black logo. Also attached.

We want the image attached on the card in some form or another- the grass/sky image.

Reason: We are extending to go over options with management- (expiring on weekend)

Reason: To finalize our design pick. We will be in touch with the designer of choice within the next day or so...the last few entries have been great- Sorry for the delay.

Reason: Working with a couple different designs trying to get finalized

Reason: Final in the workds

Marketing

• We want the image attached on the card in some form or another- the grass/sky image.

```html
<!DOCTYPE html>
<html lang="en">
<head>
<meta charset="utf-8">
<title>Lendwise Tailwind – Business Card</title>
<link rel="stylesheet" href="https://fonts.googleapis.com/css2?family=Archivo+Black&family=Questrial&display=swap">
<style>
  :root {
    --sky-top: #1b4f9c;
    --sky-mid: #4d8fd6;
    --sky-horizon: #cfe3f4;
    --grass-light: #8fd63a;
    --grass-mid: #56b020;
    --grass-dark: #2f7a12;
    --ink: #0b0b0b;
    --rule: #6b6f78;
    --white: #ffffff;
    --icon-disc: rgba(255,255,255,0.85);
    --icon-glyph: #5a9a2a;
    --brand-green: #2f9a3c;
    --panel: rgba(225,230,238,0.28);
  }
  html, body {
    margin: 0;
    padding: 0;
    overflow: hidden;
    background: #e9ecef;
  }
  .card {
    position: relative;
    width: 1200px;
    height: 720px;
    overflow: hidden;
    font-family: "Questrial", sans-serif;
  }
  .landscape {
    position: absolute;
    inset: 0;
    background:
      linear-gradient(180deg,
        var(--sky-top) 0%,
        var(--sky-mid) 35%,
        var(--sky-horizon) 64%,
        var(--grass-light) 66%,
        var(--grass-mid) 80%,
        var(--grass-dark) 100%);
  }
  .brand {
    position: absolute;
    left: 800px;
    top: 26px;
    display: flex;
    align-items: center;
    gap: 16px;
    color: var(--white);
  }
  .brand-mark {
    width: 96px;
    height: 96px;
    background: var(--brand-green);
    flex: none;
  }
  .brand-text { display: flex; flex-direction: column; }
  .brand-name {
    font-size: 31px;
    line-height: 1.05;
    letter-spacing: 0.3px;
  }
  .brand-tagline {
    margin-top: 8px;
    font-size: 20px;
  }
  .name-panel {
    position: absolute;
    left: 103px;
    top: 256px;
    width: 995px;
    height: 210px;
    background: var(--panel);
  }
  .person-name {
    position: absolute;
    left: 124px;
    top: 274px;
    margin: 0;
    font-family: "Archivo Black", sans-serif;
    font-weight: 400;
    font-size: 92px;
    line-height: 1;
    color: var(--ink);
    letter-spacing: 1px;
  }
  .name-rule {
    position: absolute;
    left: 126px;
    top: 370px;
    width: 786px;
    height: 5px;
    background: var(--rule);
  }
  .person-title {
    position: absolute;
    right: 114px;
    top: 386px;
    margin: 0;
    font-size: 32px;
    color: #161616;
  }
  .contact-rule {
    position: absolute;
    left: 103px;
    top: 505px;
    width: 4px;
    height: 188px;
    background: var(--white);
  }
  .contact-icon {
    position: absolute;
    left: 21px;
    width: 54px;
    height: 54px;
  }
  .contact-text {
    position: absolute;
    left: 117px;
    margin: 0;
    font-size: 30px;
    line-height: 35px;
    color: var(--white);
  }
</style>
</head>
<body>
<div class="card">
  <div class="landscape" role="img" aria-label="Photo of a blue sky with white clouds over a green grass field with a tractor track leading to the horizon"></div>

  <div class="brand">
    <div class="brand-mark"></div>
    <div class="brand-text">
      <span class="brand-name">Lendwise Tailwind</span>
      <span class="brand-tagline">Plan, Lend, Land.</span>
    </div>
  </div>

  <div class="name-panel"></div>
  <h1 class="person-name">Marlon Keating</h1>
  <div class="name-rule"></div>
  <p class="person-title">Product Manager</p>

  <div class="contact-rule"></div>

  <svg class="contact-icon" style="top:511px" viewBox="0 0 54 54" aria-hidden="true">
    <circle cx="27" cy="27" r="27" fill="var(--icon-disc)"/>
    <path d="M27 12c-6.6 0-11 4.8-11 10.6 0 7.6 11 19.4 11 19.4s11-11.8 11-19.4C38 16.8 33.6 12 27 12z" fill="var(--icon-glyph)"/>
    <circle cx="27" cy="22.5" r="4.2" fill="var(--white)"/>
  </svg>
  <p class="contact-text" style="top:505px">21730 W. Fieldstone Rd.<br>Northvale, MI 48167</p>

  <svg class="contact-icon" style="top:586px" viewBox="0 0 54 54" aria-hidden="true">
    <circle cx="27" cy="27" r="27" fill="var(--icon-disc)"/>
    <path d="M19 13c1.5-1 3-.6 3.8.8l2.6 4.6c.7 1.3.3 2.6-.8 3.4l-1.8 1.3c1 3 3.2 6 6 8l1.6-1.6c1-.9 2.4-1 3.4-.2l4.2 3.2c1.2.9 1.3 2.5.2 3.8-2.2 2.6-5.4 3.6-8.6 1.8-7-4-12-11-13.2-18.2-.4-3.2 1-5.6 2.6-6.9z" fill="var(--icon-glyph)"/>
  </svg>
  <p class="contact-text" style="top:596px">555.014.2290</p>

  <svg class="contact-icon" style="top:647px" viewBox="0 0 54 54" aria-hidden="true">
    <circle cx="27" cy="27" r="27" fill="var(--icon-disc)"/>
    <text x="27" y="37" text-anchor="middle" font-family="Questrial, sans-serif" font-size="30" font-weight="700" fill="var(--icon-glyph)">@</text>
  </svg>
  <p class="contact-text" style="top:657px">mkeating@lendwisecredit.com</p>
</div>
</body>
</html>
```